依頼詳細
「北辰年金事務研究連盟」の概要・活動内容等を紹介するパンフレットの作成です。パンフレットとはいえ、A4裏表の簡易版でOKです(ページ数2ページ)。全体として、固い厳粛なイメージが出ればよいかと思います。記載する文章等は添付ファイルのとおりですので、配置や色、デザイン等の作成をお願いします。アレンジはお任せします。
記載項目
北辰年金事務研究連盟/ごあいさつ/協議会概要/活動内容(原則、添付ファイルの通り)
サイズ
A4
ページ数
両面
希望イメージ
シンプル 複雑
単色 カラフル
暗い 明るい
日常 高級
遊び心 厳粛
未来的 伝統的
女性的 男性的
希望する色
青系、茶系、グレー系、全体のバランスがよければ必ずしも上記に拘らないです。
納品ファイル
• PNG形式 (.png)
補足説明
協議会のWEBサイトは以下です。
http://hokushin-renmei.net/
内容やイメージの参考にしてください。

やや硬いイメージを保ちつつ、シンプルで分かりやすいという点を判断基準として、選択いたしました。ありがとうございます。

この度は、多くのランサーの方からご提案いただき、大変ありがとうございます。改めて感謝申し上げます。
途中、修正依頼させていただいた方におかれましては、実際の選択ポイントからずれた内容で依頼してしまったこともあり、この点、お詫び申し上げます。(私以外の担当の意見も反映したことによるものです。何卒ご容赦ください。)
今後また案件が発生した際には、ご協力いただければ幸いです。
どうぞ宜しくお願いします。

```html
<!DOCTYPE html>
<html lang="ja">
<head>
<meta charset="utf-8">
<title>北辰年金事務研究連盟 活動内容・協議会概要</title>
<link href="https://fonts.googleapis.com/css2?family=Noto+Serif+JP:wght@400;600;700&family=Playfair+Display:ital,wght@1,700&display=swap" rel="stylesheet">
<style>
  :root{
    --brown-dark:#4a3526;
    --paper:#e4d9c3;
    --panel:#f3ede1;
    --ink:#3b2c22;
    --cell-head:#b3a796;
    --cell-body:#f7f3eb;
    --rule:#ffffff;
  }
  *{margin:0;padding:0;box-sizing:border-box}
  html,body{width:848px;height:1200px;overflow:hidden}
  body{
    background:var(--paper);
    font-family:"Noto Serif JP",serif;
    color:var(--ink);
    position:relative;
  }
  .band{position:absolute;left:0;width:848px;background:var(--brown-dark)}
  .band--top{top:0;height:48px}
  .band--middle{top:576px;height:30px}
  .band--bottom{top:1140px;height:40px}

  .activities{
    position:absolute;left:42px;top:48px;width:764px;height:500px;
    background:var(--panel);
    border-radius:0 0 26px 26px;
    box-shadow:0 2px 6px rgba(74,53,38,.15);
  }
  .section-label{
    position:absolute;left:50%;transform:translateX(-50%);
    width:180px;height:38px;
    background:var(--brown-dark);
    color:#fff;font-weight:700;font-size:21px;letter-spacing:.35em;
    display:flex;align-items:center;justify-content:center;
    outline:1px solid var(--brown-dark);outline-offset:3px;
    padding-left:.35em;
  }
  .activities .section-label{top:22px}
  .overview-label{top:640px}

  .activity{position:absolute;left:70px;width:640px}
  .activity__num{
    position:absolute;left:0;top:-14px;
    font-family:"Playfair Display",serif;font-style:italic;font-weight:700;
    font-size:54px;color:var(--brown-dark);line-height:1;
  }
  .activity__title{margin-left:44px;font-size:17px;font-weight:700;letter-spacing:.04em}
  .activity__body{margin:12px 0 0 44px;font-size:13.5px;line-height:2}
  .activity--1{top:112px}
  .activity--2{top:280px}
  .activity--3{top:388px}

  .overview{
    position:absolute;left:160px;top:702px;width:545px;
    border-collapse:collapse;font-size:12px;
  }
  .overview th,.overview td{border:2px solid var(--rule);padding:3px 12px;vertical-align:middle;line-height:1.5}
  .overview th{
    width:218px;background:var(--cell-head);color:var(--ink);
    font-weight:600;text-align:center;letter-spacing:.3em;
  }
  .overview td{background:var(--cell-body)}
  .overview tr{height:30px}
  .overview tr.row--purpose{height:74px}
  .overview tr.row--office{height:66px}
</style>
</head>
<body>
  <div class="band band--top"></div>

  <section class="activities">
    <h2 class="section-label">活動内容</h2>

    <div class="activity activity--1">
      <span class="activity__num">1</span>
      <h3 class="activity__title">社会保険加入促進の啓蒙活動</h3>
      <p class="activity__body">協議会所属の社会保険労務士によるセミナーの開催（自主開催）<br>
      集客団体様向けのセミナー・勉強会の提案<br>
      その他適正加入の啓発活動</p>
    </div>

    <div class="activity activity--2">
      <span class="activity__num">2</span>
      <h3 class="activity__title">社会保険調査リスク診断のご提供</h3>
      <p class="activity__body">保険料負担上の問題点、保険料負担・法的リスクに関する診断サービス</p>
    </div>

    <div class="activity activity--3">
      <span class="activity__num">3</span>
      <h3 class="activity__title">社会保険調査対応＆コンサルティング</h3>
      <p class="activity__body">出頭通知書対応・社会保険調査対応の専門家として、的確な指導・助言の実施<br>
      各企業様の実情を踏まえた、コンサルティングサービスのご提供</p>
    </div>
  </section>

  <div class="band band--middle"></div>

  <h2 class="section-label overview-label">協議会概要</h2>

  <table class="overview">
    <tr><th>団体名</th><td>北辰年金事務研究連盟</td></tr>
    <tr class="row--purpose"><th>趣旨</th><td>社会保険の適正な加入を推進し、企業と従業員双方の安心を守るため、調査対応の知識と経験を持つ社会保険労務士が連携して活動します。</td></tr>
    <tr><th>代表</th><td>社会保険労務士 森田 誠（青葉総合事務所）</td></tr>
    <tr><th>副代表</th><td>社会保険労務士 川原 直子（川原労務管理室）</td></tr>
    <tr><th>相談アドバイザー</th><td>元年金事務所 調査担当 高見 修</td></tr>
    <tr><th>設立</th><td>2012年</td></tr>
    <tr><th>所属社会保険労務士</th><td>全国 13都道府県 18名</td></tr>
    <tr class="row--office"><th>事務局</th><td>〒100-0000 東京都千代田区北辰町2丁目4番<br>北辰ビル5階<br>青葉総合事務所内</td></tr>
    <tr><th>TEL</th><td>03-0000-0000（平日 9:00〜17:00）</td></tr>
    <tr><th>FAX</th><td>03-0000-0001</td></tr>
  </table>

  <div class="band band--bottom"></div>
</body>
</html>
```